PREMIUM AGENCY High End Business Card - A+++ Designers Wanted

** DO NOT ATTEMPT TO CONTACT ME THROUGH SEARCHING ON GOOGLE OR EMAILING ME THROUGH MY WEBSITE **

I need a fresh, contemporary business card designed using the logo attached (VOLKRANE)

I have attached the font for VOLKRANE

It must have a premium look and feel. The business card size must be STANDARD size.

You can submit either/both VERTICAL or HORIZONTAL designs.

FRONT: It must have the following sample information on

Peter Dowle
Director Operations
Mobile +61 452 000 000
Email peterdowle@volkrane.example
www.volkrane.example

The REAR of the business card must have the words

CREATE INSPIRE TOMORROW

as part of the design, in the same font (NEXA) attached.

The words do not need to be in capitals, or on the same line, please design this as you see it best working.

ADDITIONAL INFORMATION
======================

The VOLKRANE logo must be on the front of the card

I want Ultraviolet printing on the final design, to enhance either the NAME of the person OR the VOLKRANE logo OR the words on the back of the card.

Target Market(s)

Agency, Advertising Agency, Creative, Designers

Industry/Entity Type

Media

Contact Information for Business Card

Design Agency, Contemporary, Premium look and feel, High Quality

Font styles to use
Serif
Sans Serif
Other font styles liked:
• ATTACHED TO PROJECT

Requirements
Must have
• BLACK & WHITE as the primary design, and if you feel there can be a highlighted colour, then this can be used.
• The Logo ICON attached is blue, this colour must not be changed.
• I have attached the partner brand VOLKRANE MEDIA incase you need to manipulate the original files.
• ** DO NOT ATTEMPT TO CONTACT ME THROUGH SEARCHING ON GOOGLE OR EMAILING ME THROUGH MY WEBSITE **
Nice to have
• Must be Premium. I have attached some sample designs, that I like that would be a good inspiration for where this can be taken.
• My favourite design is is the SNAPFRAME2-BUSINESSCARD-TEMPLATE
Should not have
• No funny or silly standard / off the shelf designs

```html
<!DOCTYPE html>
<html lang="en">
<head>
<meta charset="utf-8">
<title>Volkrane Media – Business Card</title>
<link rel="stylesheet" href="https://fonts.googleapis.com/css2?family=Montserrat:wght@400;500;600&family=Roboto:wght@400&display=swap">
<style>
  :root {
    --backdrop: #a8a5a5;
    --card: #363939;
    --accent: #3b90cc;
    --ink: #f2f2f2;
    --ink-soft: #e3e3e3;
  }
  * { margin: 0; padding: 0; box-sizing: border-box; }
  html, body {
    width: 1200px; height: 1200px; overflow: hidden;
    background: var(--backdrop);
  }
  .canvas { position: relative; width: 1200px; height: 1200px; }
  .card {
    position: absolute;
    width: 714px; height: 420px;
    background: var(--card);
    overflow: hidden;
  }
  .card--rear  { left: 238px; top: 117px; }
  .card--front { left: 230px; top: 642px; }

  .brand-mark {
    position: absolute;
    font-family: "Montserrat", sans-serif;
    font-weight: 600;
    color: var(--accent);
    letter-spacing: 0.06em;
    display: flex; align-items: center; gap: 10px;
    white-space: nowrap;
  }
  .brand-mark__dot {
    width: 14px; height: 14px; border-radius: 50%;
    background: var(--accent);
  }
  .card--rear .brand-mark {
    left: 0; right: 0; top: 168px;
    justify-content: center;
    font-size: 34px;
  }
  .tagline {
    position: absolute; left: 0; right: 0; top: 232px;
    text-align: center;
    font-family: "Montserrat", sans-serif;
    font-weight: 400;
    font-size: 15px;
    letter-spacing: 0.32em;
    color: var(--ink-soft);
    white-space: nowrap;
  }
  .card--front .brand-mark {
    left: 112px; top: 160px;
    font-size: 24px;
  }

  .contact {
    position: absolute; left: 358px; top: 86px;
    font-family: "Roboto", sans-serif;
  }
  .contact__name {
    font-family: "Montserrat", sans-serif;
    font-weight: 500;
    font-size: 27px;
    color: var(--accent);
    letter-spacing: 0.01em;
    white-space: nowrap;
  }
  .contact__role {
    margin-top: 6px;
    font-size: 15px; color: var(--ink-soft);
  }
  .contact__list { list-style: none; margin-top: 40px; }
  .contact__item {
    display: flex; align-items: center;
    height: 27.5px;
    font-size: 18px; color: var(--ink-soft);
    white-space: nowrap;
  }
  .contact__icon { width: 17px; height: 17px; margin-right: 18px; fill: var(--accent); flex: none; }

  .accent-bar {
    position: absolute; left: 0; top: 369px;
    width: 331px; height: 14px;
    background: var(--accent);
  }
  .wordmark {
    position: absolute; right: 38px; top: 358px;
    font-family: "Montserrat", sans-serif;
    font-weight: 500;
    font-size: 27px;
    letter-spacing: 0.09em;
    color: var(--ink);
    white-space: nowrap;
  }
</style>
</head>
<body>
<main class="canvas">
  <section class="card card--rear" aria-label="Card rear">
    <div class="brand-mark"><span class="brand-mark__dot"></span>VOLKRANE</div>
    <p class="tagline">CREATE INSPIRE TOMORROW</p>
  </section>

  <section class="card card--front" aria-label="Card front">
    <div class="brand-mark"><span class="brand-mark__dot"></span>VOLKRANE</div>

    <div class="contact">
      <p class="contact__name">Peter Dowle</p>
      <p class="contact__role">Director Operations</p>
      <ul class="contact__list">
        <li class="contact__item">
          <svg class="contact__icon" viewBox="0 0 20 20" aria-hidden="true"><path d="M2 7c0-3 4-4 8-4s8 1 8 4v2h-4V7H6v2H2z"/><path d="M5 10h10l2 7H3z"/></svg>
          +61 452 000 000
        </li>
        <li class="contact__item">
          <svg class="contact__icon" viewBox="0 0 20 20" aria-hidden="true"><path d="M2 5h16v11H2z M3 6l7 6 7-6v1l-7 6-7-6z" fill-rule="evenodd"/></svg>
          peterdowle@volkrane.example
        </li>
        <li class="contact__item">
          <svg class="contact__icon" viewBox="0 0 20 20" aria-hidden="true"><circle cx="10" cy="10" r="7.5" fill="none" stroke="#3b90cc" stroke-width="1.6"/><ellipse cx="10" cy="10" rx="3.2" ry="7.5" fill="none" stroke="#3b90cc" stroke-width="1.4"/><path d="M2.5 10h15M4 6h12M4 14h12" stroke="#3b90cc" stroke-width="1.2"/></svg>
          www.volkrane.example
        </li>
      </ul>
    </div>

    <div class="accent-bar"></div>
    <p class="wordmark">VOLKRANE MEDIA</p>
  </section>
</main>
</body>
</html>
```